Shipping and Logistics, Project

Project description : Company Profile

A total logistics company covering domestic / international freight forwarding, warehouse management services, haulage, supply chain management, transport management & distribution, procurement & assembly services, shipping, chartering & bunker services, project logistics & tax exemption consultancy, oil & gas logistics, halal logistics services & integrated logistics management. We’re a well-established and experienced freight forwarder in Kuala Lumpur, Malaysia. We specialize in customized value-added solution that optimizes your supply chain by trimming inventory, reducing logistics cost and enhancing your customer service levels.

As a member of the Worldwide Carrier and Haulage Alliance which comprise of 170 global freight agents in 80 countries that promotes great handling in cross-trade logistics and freighting. You could rely on our efficiency in handlings of export cargo (FCL, LCL, Bulk and Conventional) between our global network offices worldwide with a total scale of 10,000 groomed specialists in various logistics division working together to ensure delivery task meets with your expectation. With our dedicated qualified and experienced professionals, we are fully committed to serving our clients.

Our generic services are listed below for your reference:

• Air Freight
• Ocean Freight FCL & LCL
• Container Haulage
• Warehousing
• Transportation and Distribution within Malaysia and Thailand
• Cross-Border Road Line-hauls between Thailand, Malaysia, Singapore and Laos
• Customs Brokerage and Forwarding
• Project Cargo Freight Forwarding for setting up of new plants / factories and ad hoc heavy-lift
• Air-Sea-Road-Rail multi-modal options
• Import / Export / Storage / Documentation / Handling of DG / Hazmat
• Vessel and Aircraft Charters

Our Mission
Based on the motto “Quick, Reliable and Polite”, we are dedicated to upholding the following three points corporate philosophy:
1. Adhering to the principle that “the customer always comes first”.
2. Contributing to the development of the local community.
3. Making it our duty to be responsible and sincere.

Our Edge
• One-Stop Logistics Solutions
• Extensive Network Throughout Malaysia
• Highly Qualified and Experienced Pool of Professionals
• Comprehensive IT Solutions
• Innovative and Customer-focused Solutions
• Flexible and Consistent in Managing Exceptions
• Total Supply Chain Visibility

Target Market
1. We sell the logistics services to all the industry in Malaysia and Worldwide. (ONE Stop Logistics Solutions)

Competitor
1. RT Volmaren
2. Corvella Transport
3. Brandt + Osswig
4. VELIRO
5. TZQ
6. Farrowline
7. Ruma Logistics

Rules for Picking a Company Name
1. Unique and unforgettable
2. Avoid unusual spellings
3. Easy to pronounce and remember
4. Keep it simple
5. Make some sense
6. Give a clue

Rules for Picking a Company Logo
4. Keep it simple
5. Make some sense
6. Give a clue

1. Simplicity
2. Memorability
3. Originality
4. Modern Yet Timeless
5. Balance
6. Complementary
7. Versatility

Stationery Information
1. Company Name : Tepiandek Solutions Sdn Bhd
2. Company Registration : 2730518-W
3. Address : 14-07, Jalan Seroja Indah 5, Taman Bukit Seroja, 81300 Johor Bahru, Johor, Malaysia.
4. Name : Derek Tan
5. Position : Manager
6. Mobile No : (+6019) 4308127
7. Office No : (+607) 5129870
8. Fax No : Not Available
9. Email Address : derek.tan@tepiandek-freight.example
10. Web Domain : www.tepiandek-freight.example
11. Company Slogan : Be Globally Connected

Target Market(s)

Corporate Company

Industry/Entity Type

Shipping and Logistics Industry

Requirements
Must have
• Company Full Name : TEPIANDEK SOLUTIONS SDN. BHD.
Nice to have
• Keep it simple and unforgettable ...

```html
<!DOCTYPE html>
<html lang="en">
<head>
<meta charset="utf-8">
<title>Tepiandek Solutions Stationery</title>
<link href="https://fonts.googleapis.com/css2?family=Lato:wght@400;700&display=swap" rel="stylesheet">
<style>
:root{
  --bg:#b5b5b5;
  --paper:#ffffff;
  --blue:#3a86c8;
  --dark:#2b2b2b;
  --ink:#1f1f1f;
  --faint:#e3edf7;
}
*{margin:0;padding:0;box-sizing:border-box}
html,body{width:1200px;height:1200px;overflow:hidden;background:var(--bg);font-family:'Lato',sans-serif;color:var(--ink)}
.sheet{position:absolute;background:var(--paper);box-shadow:0 2px 6px rgba(0,0,0,.25);overflow:hidden}
.card{width:304px;height:174px}
.name{position:absolute;font-size:11.5px;font-weight:400}
.role{position:absolute;font-size:8.5px}
.contact{position:absolute;font-size:9.6px;line-height:13px}
.contact .gap{height:6px}
.contact b{font-weight:400;color:var(--blue)}
.brand{position:absolute;display:flex;align-items:center;gap:5px;font-weight:700;color:var(--blue);letter-spacing:.5px;white-space:nowrap}
.brand i{display:block;background:var(--blue)}
.divider{position:absolute;width:1px;background:var(--blue)}
.faint-disc{position:absolute;border-radius:50%;border:10px solid var(--faint)}
</style>
</head>
<body>

<!-- Card 1 -->
<div class="sheet card" style="left:119px;top:112px">
  <div class="name" style="left:18px;top:16px">Derek Tan</div>
  <div class="role" style="left:18px;top:32px">Manager</div>
  <div class="faint-disc" style="left:198px;top:45px;width:104px;height:104px"></div>
  <div class="contact" style="left:18px;top:100px">
    <div><b>M:</b> (+6019) 4308127</div><div><b>P:</b> (+607) 5129870</div>
    <div class="gap"></div>
    <div><b>E:</b> derek.tan@tepiandek-freight.example</div><div><b>W:</b> www.tepiandek-freight.example</div>
  </div>
</div>

<!-- Card 2 -->
<div class="sheet card" style="left:450px;top:112px;width:306px">
  <div style="position:absolute;left:17px;top:16px;font-size:11.5px;color:var(--blue)">Derek Tan <span style="color:#555;font-size:8.5px">&nbsp;|&nbsp; Manager</span></div>
  <div style="position:absolute;left:0;top:60px;width:80px;height:114px;background:var(--blue)"></div>
  <div class="contact" style="left:128px;top:94px;line-height:15px">
    <div><svg width="10" height="10" viewBox="0 0 10 10"><circle cx="5" cy="5" r="5" fill="var(--blue)"/><rect x="3.5" y="2.2" width="3" height="5.6" rx=".6" fill="#fff"/></svg> (+6019) 4308127</div>
    <div><svg width="10" height="10" viewBox="0 0 10 10"><circle cx="5" cy="5" r="5" fill="var(--blue)"/><path d="M3 3 Q3 7 7 7" stroke="#fff" stroke-width="1.4" fill="none"/></svg> (+607) 5129870</div>
    <div class="gap"></div>
    <div><svg width="10" height="10" viewBox="0 0 10 10"><circle cx="5" cy="5" r="5" fill="var(--blue)"/><text x="5" y="7.3" font-size="7" text-anchor="middle" fill="#fff" font-family="Lato">@</text></svg> derek.tan@tepiandek-freight.example</div>
    <div><svg width="10" height="10" viewBox="0 0 10 10"><circle cx="5" cy="5" r="5" fill="var(--blue)"/><circle cx="5" cy="5" r="3" stroke="#fff" stroke-width=".8" fill="none"/><path d="M2 5h6M5 2v6" stroke="#fff" stroke-width=".7"/></svg> www.tepiandek-freight.example</div>
  </div>
</div>

<!-- Card 3 -->
<div class="sheet card" style="left:784px;top:112px">
  <div class="brand" style="left:18px;top:83px;font-size:10.5px"><i style="width:9px;height:9px"></i>TEPIANDEK</div>
  <div class="divider" style="left:120px;top:38px;height:98px"></div>
  <div class="name" style="left:132px;top:38px">Derek Tan</div>
  <div class="role" style="left:132px;top:54px">Manager</div>
  <div class="contact" style="left:132px;top:78px">
    <div><b>M:</b> (+6019) 4308127</div><div><b>P:</b> (+607) 5129870</div>
    <div class="gap"></div>
    <div><b>E:</b> derek.tan@tepiandek-freight.example</div><div><b>W:</b> www.tepiandek-freight.example</div>
  </div>
  <svg style="position:absolute;left:0;bottom:0" width="304" height="15"><polygon points="0,0 88,0 80,15 0,15" fill="var(--dark)"/><polygon points="92,0 304,0 304,15 84,15" fill="var(--blue)"/></svg>
</div>

<!-- Card 4 -->
<div class="sheet card" style="left:119px;top:303px">
  <div class="name" style="left:19px;top:17px">Derek Tan</div>
  <div class="role" style="left:19px;top:33px">Manager</div>
  <div class="brand" style="left:22px;top:118px;font-size:10px"><i style="width:8px;height:8px"></i>TEPIANDEK</div>
  <div class="divider" style="left:122px;top:92px;height:63px"></div>
  <div class="contact" style="left:128px;top:92px">
    <div><b>M:</b> (+6019) 4308127</div><div><b>P:</b> (+607) 5129870</div>
    <div class="gap"></div>
    <div><b>E:</b> derek.tan@tepiandek-freight.example</div><div><b>W:</b> www.tepiandek-freight.example</div>
  </div>
</div>

<!-- Card 5 -->
<div class="sheet card" style="left:450px;top:302px;width:306px;background:var(--dark)" role="img" aria-label="Dark card back with a tonal repeating pattern">
  <div class="brand" style="left:0;right:0;top:78px;justify-content:center;font-size:16px;color:#fff"><i style="width:12px;height:12px;background:#fff"></i>TEPIANDEK</div>
</div>

<!-- Card 6 -->
<div class="sheet card" style="left:784px;top:303px">
  <div class="brand" style="left:0;right:0;top:72px;justify-content:center;font-size:24px"><i style="width:18px;height:18px"></i>TEPIANDEK</div>
</div>

<!-- Letterhead -->
<div class="sheet" style="left:119px;top:520px;width:407px;height:574px">
  <svg style="position:absolute;right:0;top:0" width="190" height="30"><polygon points="0,0 190,0 190,22 55,30" fill="var(--blue)"/></svg>
  <div style="position:absolute;right:26px;top:9px;color:#fff;font-size:8.5px">BE GLOBALLY CONNECTED</div>
  <div class="brand" style="left:28px;top:28px;font-size:15px"><i style="width:12px;height:12px"></i>TEPIANDEK</div>
  <div class="faint-disc" style="left:135px;top:195px;width:135px;height:135px;border-width:12px;opacity:.8"></div>
  <div style="position:absolute;left:28px;top:82px;width:355px;font-size:7.3px;line-height:14.3px">
    <div style="font-weight:700">To<br>Lorem Ipsum is simply<br>Lorem Ipsum is Lorem Ipsum is<br>Lorem Ipsum is</div>
    <p style="margin-top:14px">&nbsp;dummy text of the printing and typesetting industry. Lorem Ipsum has been the industry's standard dummy text ever since the 1500s, when an unknown printer took a galley of type and scrambled it to make a type specimen book. It has survived not only five centuries, but also the leap into electronic typesetting, remaining essentially unchanged.</p>
    <p style="margin-top:14px">It is a long established fact that a reader will be distracted by the readable content of a page when looking at its layout. The point of using Lorem Ipsum is that it has a more-or-less normal distribution of letters, as opposed to using 'Content here, content here', making it look like readable English. Many desktop publishing packages and web page editors now use Lorem Ipsum as their default model text, and a search for 'lorem .</p>
    <p style="margin-top:14px">&nbsp;Contrary to popular belief, Lorem Ipsum is not simply random text. It has roots in a piece of classical Latin literature from 45 BC, making it over 2000 years old. Richard Calloway, a Latin professor at Hollowbrook College, looked up one of the more obscure Latin words, consectetur, from a Lorem Ipsum passage,</p>
    <p style="margin-top:14px">Lorem Ipsum</p>
    <div role="img" aria-label="Handwritten signature" style="width:88px;height:40px;margin:4px 0 2px;background:linear-gradient(90deg,#eee,#f6f6f6)"></div>
    <p>Lorem Ipsum is a dummy</p>
  </div>
  <div style="position:absolute;left:0;right:0;top:528px;text-align:center;font-size:5px;color:var(--blue)">Tepiandek Solutions Sdn. Bhd. &nbsp;&nbsp;| &nbsp;&nbsp;Regn#: 2730518-W</div>
  <div style="position:absolute;left:0;right:0;top:538px;height:2px;background:var(--blue)"></div>
  <div style="position:absolute;left:0;right:0;top:540px;height:34px;background:var(--dark);color:#fff;font-size:5px;line-height:7.5px">
    <div style="position:absolute;left:53px;top:10px">M: (+6019) 4308127<br>P: (+607) 5129870</div>
    <div style="position:absolute;left:111px;top:8px;width:1px;height:17px;background:var(--blue)"></div>
    <div style="position:absolute;left:120px;top:10px">E: derek.tan@tepiandek-freight.example<br>W: www.tepiandek-freight.example</div>
    <div style="position:absolute;left:217px;top:8px;width:1px;height:17px;background:var(--blue)"></div>
    <div style="position:absolute;left:229px;top:10px">14-07, Jalan Seroja Indah 5, Taman Bukit Seroja,<br>81300 Johor Bahru, Johor, Malaysia.</div>
  </div>
</div>

<!-- Envelope front -->
<div class="sheet" style="left:584px;top:556px;width:504px;height:227px">
  <div class="brand" style="left:22px;top:25px;font-size:10.5px"><i style="width:9px;height:9px"></i>TEPIANDEK</div>
  <div style="position:absolute;left:23px;top:56px;font-size:5.6px;line-height:8.4px;width:100px">14-07, Jalan Seroja Indah 5, Taman Bukit Seroja, 81300 Johor Bahru, Johor, Malaysia.</div>
  <div class="faint-disc" style="left:378px;top:48px;width:114px;height:114px;border-width:12px"></div>
  <div style="position:absolute;left:0;right:0;top:199px;height:4px;background:var(--blue)"></div>
  <div style="position:absolute;left:0;right:0;top:204px;height:23px;background:var(--dark)"></div>
</div>

<!-- Envelope back -->
<div class="sheet" style="left:584px;top:811px;width:504px;height:226px">
  <svg style="position:absolute;left:0;top:0" width="504" height="60"><path d="M0 0H504V25L275 54Q252 58 229 54L0 25Z" fill="var(--dark)"/></svg>
  <div class="brand" style="left:0;right:0;top:20px;justify-content:center;font-size:9px">TEPIANDEK</div>
</div>

</body>
</html>
```